Appraisal and Umpire Services for Property Damage Insurance Claims

I need a banner design that I can post as an advertisement on industry web pages. I would like this to be elegant and reflective of quality, integrity and professionalism.

Target Market(s)

Insurance Companies and Attorneys

Industry/Entity Type

Insurance

Contact Information for Business Card

Gerald M. Hollis
918 Birchwell Lane
PO Box 582
Clifton Park, NY 12093
ghollis@brindlevault.com
Phone: (800) 555-0147, Ext. 2861
Direct: (315) 555-0189

Logo Text

Line One: Velmar Brook Claim Service, Inc. Line two: Appraisal and Umpire Services

Font styles to use
Serif
Sans Serif

Colors
0255a3
f78f20
faa54b
3176b5

Requirements
Must have
• New Logo and matching banner, business card and stationary.
• The colors must be orange and navy blue in the logo. I have selected them below.

```html
<!DOCTYPE html>
<html lang="en">
<head>
<meta charset="utf-8">
<title>Velmar Brook Claim Service – Appraisal and Umpire Service Banner</title>
<link rel="stylesheet" href="https://fonts.googleapis.com/css2?family=Barlow:wght@400;500;600;700&display=swap">
<style>
  :root {
    --stage: #5a5a5a;
    --white: #ffffff;
    --navy: #0255a3;
    --navy-deep: #023f86;
    --sky: #0c93d2;
    --sky-soft: #0a80c4;
    --orange: #f78f20;
    --orange-light: #faa54b;
    --orange-dark: #a85a14;
    --ink: #1e2658;
    --grey: #8a8c92;
  }
  html, body {
    margin: 0;
    padding: 0;
    width: 1200px;
    height: 868px;
    overflow: hidden;
    background: var(--stage);
    font-family: "Barlow", Arial, sans-serif;
  }
  .banner {
    position: absolute;
    left: 106px;
    top: 260px;
    width: 989px;
    height: 345px;
    display: block;
  }
  .headline { font-weight: 700; fill: var(--white); letter-spacing: 0.5px; }
  .headline-small { font-weight: 700; fill: var(--ink); }
  .agent-name { font-weight: 700; fill: var(--orange-light); }
  .contact { font-weight: 500; fill: var(--white); }
  .brand-name { font-weight: 700; fill: var(--ink); }
  .brand-line { font-weight: 500; fill: var(--grey); letter-spacing: 1.5px; }
  .icon { fill: var(--sky); }
  .icon-stroke { fill: none; stroke: var(--sky); stroke-width: 1.6; stroke-linecap: round; }
</style>
</head>
<body>
<svg class="banner" viewBox="0 0 799 279" preserveAspectRatio="none" aria-label="Velmar Brook Claim Service appraisal and umpire service banner">
  <defs>
    <linearGradient id="bandSky" x1="0" y1="0" x2="1" y2="0">
      <stop offset="0" stop-color="var(--sky-soft)"/>
      <stop offset="1" stop-color="var(--sky)"/>
    </linearGradient>
    <linearGradient id="bandNavy" x1="0" y1="0" x2="1" y2="1">
      <stop offset="0" stop-color="var(--navy-deep)"/>
      <stop offset="1" stop-color="var(--navy)"/>
    </linearGradient>
    <clipPath id="panelClip">
      <polygon points="290,0 799,0 799,279 324,279 304,262 355,110"/>
    </clipPath>
  </defs>

  <rect class="brand-field" x="0" y="0" width="799" height="279" fill="var(--white)"/>

  <g class="info-panel" clip-path="url(#panelClip)">
    <rect x="280" y="0" width="519" height="106" fill="url(#bandSky)"/>
    <rect x="280" y="106" width="519" height="173" fill="url(#bandNavy)"/>
  </g>

  <polygon class="accent-top" points="230,0 290,0 355,110" fill="var(--orange)"/>
  <polygon class="accent-fold" points="355,110 262,232 304,262" fill="var(--orange-dark)"/>
  <polygon class="accent-bottom" points="262,232 251,279 324,279 304,262" fill="var(--orange)"/>

  <g class="brand">
    <text class="brand-name" x="148" y="139" font-size="36" text-anchor="middle">VELMAR BROOK</text>
    <text class="brand-line" x="148" y="168" font-size="20" text-anchor="middle">CLAIM SERVICE, INC</text>
  </g>

  <g class="service-title">
    <text x="384" y="51" font-size="40"><tspan class="headline">APPRAISAL</tspan><tspan class="headline-small" font-size="27" dx="6">AND</tspan></text>
    <text class="headline" x="382" y="91" font-size="40">UMPIRE SERVICE</text>
  </g>

  <text class="agent-name" x="382" y="171" font-size="40">Gerald M. Hollis</text>

  <g class="contact-line">
    <rect class="icon" x="385" y="197" width="17" height="12" rx="1"/>
    <polyline points="385,198 393.5,205 402,198" fill="none" stroke="var(--navy)" stroke-width="1.4"/>
    <text class="contact" x="410" y="209" font-size="18">ghollis@brindlevault.com</text>
  </g>
  <g class="contact-line">
    <path class="icon" d="M386 233 q2 -4 5 -2 l2 3 q1 2 -1 3 q1 3 4 5 q1 -2 3 -1 l3 2 q2 3 -2 5 q-6 2 -11 -4 q-4 -5 -3 -11z"/>
    <path class="icon-stroke" d="M396 232 a5 5 0 0 1 5 5 M396 228 a9 9 0 0 1 9 9"/>
    <text class="contact" x="410" y="245" font-size="18">(800) 555-0147, Ext. 2861</text>
  </g>
</svg>
</body>
</html>
```